Business Card and Stationary for Scuba Dive Company and UW Photography
Deep Reef Co
Modern
Capt. Dan Hollis
CEO
4810 Harbor Ct
Dunedin FL 34512
capt.dan@deeprfco.com
www.deeprfco.com
Master Captain, QDTA IDC Staff Instructor
Would also like another card for:
Greta Wenslow
greta@deeprfco.com
Company is focused on Scuba Diving Trips, Travel and Underwater Photography. Will be selling our photos and canvas. Will focus on dive charters and trips specializing in underwater photography.

```html
<!DOCTYPE html>
<html lang="en">
<head>
<meta charset="utf-8">
<title>Deep Reef Co — Stationery Set</title>
<link rel="stylesheet" href="https://fonts.googleapis.com/css2?family=Montserrat:wght@400;600&display=swap">
<style>
:root{
  --bg:#e7e4df;
  --paper:#ffffff;
  --navy:#0b1a33;
  --deep:#12315e;
  --ocean:#2f7fd0;
  --sky:#8fc3ef;
  --ink:#34475f;
  --muted:#8a96a5;
  --grey:#7d7f83;
  --pale:#dfe2e6;
  --black:#141518;
}
*{box-sizing:border-box;margin:0;padding:0}
html,body{width:1200px;height:490px;overflow:hidden;background:var(--bg);font-family:"Montserrat",sans-serif;color:var(--ink)}
.canvas{position:relative;width:1200px;height:490px}
.piece{position:absolute;box-shadow:0 2px 6px rgba(0,0,0,.18)}

.brand{display:flex;align-items:center;gap:5px;font-weight:600;letter-spacing:.04em;white-space:nowrap}
.brand-dot{width:7px;height:7px;border-radius:50%;background:var(--ocean)}

/* business cards */
.card{left:19px;width:130px;height:70px;border-radius:3px;overflow:hidden}
.card-dark{background:linear-gradient(135deg,var(--navy),var(--deep) 70%,var(--ocean))}
.card-dark .brand{position:absolute;left:8px;top:10px;font-size:7px;color:#fff}
.card-contact{position:absolute;right:7px;top:9px;text-align:right;color:#fff;font-size:4.5px;line-height:1.45}
.card-contact .name{font-size:6px;font-weight:600}
.card-web{position:absolute;left:8px;bottom:7px;font-size:4.5px;color:var(--sky)}
.card-light{background:linear-gradient(180deg,#f4f5f6,var(--pale));}
.card-light .lines{position:absolute;left:10px;right:10px;top:18px}
.card-light .lines span{display:block;height:1px;background:#c2c7cd;margin-bottom:9px}
.card-light .tag{position:absolute;left:10px;bottom:8px;font-size:4.5px;color:var(--muted)}
.card-white{background:var(--paper)}
.card-white .mark{position:absolute;left:18px;top:12px;width:94px;height:46px}
.card-white .brand{position:absolute;right:8px;bottom:7px;font-size:5px;color:var(--ocean)}

/* letterheads */
.letterhead{top:12px;width:308px;height:444px;background:var(--paper)}
.lh-head{position:absolute;left:118px;top:22px}
.lh-head .brand{font-size:10px;color:var(--ocean)}
.lh-address{position:absolute;right:20px;top:20px;text-align:right;font-size:5px;line-height:1.5;color:var(--muted)}
.lh-mark{position:absolute;left:40px;top:150px;width:200px;height:190px}
.lh-band{position:absolute;left:0;right:0;bottom:16px;height:8px;background:linear-gradient(90deg,var(--deep),var(--ocean),var(--sky),var(--ocean),var(--deep))}
.lh-foot{position:absolute;left:0;right:0;bottom:28px;text-align:center;font-size:4.5px;color:var(--muted);letter-spacing:.05em}

/* envelopes */
.flap{left:828px;width:353px;overflow:hidden}
.flap svg{display:block;width:100%;height:100%}
.flap .brand{position:absolute;left:120px;top:18px;font-size:7px}
.envelope{left:828px;top:360px;width:353px;height:116px;background:var(--paper)}
.envelope .brand{position:absolute;left:16px;top:14px;font-size:7px;color:var(--ocean)}
.envelope .ret{position:absolute;left:16px;top:26px;font-size:4.5px;color:var(--muted)}
.envelope .mark{position:absolute;right:14px;bottom:10px;width:120px;height:70px}
.mark-fill{border-radius:50%;background:radial-gradient(ellipse at center,rgba(143,195,239,.35),rgba(143,195,239,0) 70%)}
</style>
</head>
<body>
<main class="canvas">

  <!-- business cards -->
  <section class="piece card card-dark" style="top:29px">
    <div class="brand"><span class="brand-dot"></span>Deep Reef Co</div>
    <div class="card-contact"><div class="name">Capt. Dan Hollis</div>CEO<br>4810 Harbor Ct<br>Dunedin FL 34512<br>capt.dan@deeprfco.com</div>
    <div class="card-web">www.deeprfco.com</div>
  </section>
  <section class="piece card card-dark" style="top:123px">
    <div class="brand"><span class="brand-dot"></span>Deep Reef Co</div>
    <div class="card-contact"><div class="name">Capt. Dan Hollis</div>Master Captain<br>QDTA IDC Staff Instructor<br>capt.dan@deeprfco.com</div>
    <div class="card-web">www.deeprfco.com</div>
  </section>
  <section class="piece card card-dark" style="top:211px">
    <div class="brand"><span class="brand-dot"></span>Deep Reef Co</div>
    <div class="card-contact"><div class="name">Greta Wenslow</div>greta@deeprfco.com<br>www.deeprfco.com</div>
    <div class="card-web">www.deeprfco.com</div>
  </section>
  <section class="piece card card-light" style="top:298px">
    <div class="lines"><span></span><span></span><span></span></div>
    <div class="tag">Dive charters and photo trips</div>
  </section>
  <section class="piece card card-white" style="top:378px">
    <div class="mark mark-fill" role="img" aria-label="Faint hammerhead shark line illustration"></div>
    <div class="brand"><span class="brand-dot"></span>Deep Reef Co</div>
  </section>

  <!-- letterheads -->
  <section class="piece letterhead" style="left:173px">
    <div class="lh-head"><div class="brand"><span class="brand-dot"></span>Deep Reef Co</div></div>
    <div class="lh-address">4810 Harbor Ct<br>Dunedin FL 34512<br>capt.dan@deeprfco.com<br>www.deeprfco.com</div>
    <div class="lh-mark mark-fill" role="img" aria-label="Large faint hammerhead shark line illustration"></div>
    <div class="lh-foot">www.deeprfco.com</div>
    <div class="lh-band"></div>
  </section>
  <section class="piece letterhead" style="left:499px">
    <div class="lh-head"><div class="brand"><span class="brand-dot"></span>Deep Reef Co</div></div>
    <div class="lh-mark mark-fill" role="img" aria-label="Large faint hammerhead shark line illustration"></div>
    <div class="lh-foot">4810 Harbor Ct · Dunedin FL 34512 · www.deeprfco.com</div>
    <div class="lh-band"></div>
  </section>

  <!-- envelope flaps -->
  <section class="piece flap" style="top:12px;height:100px;box-shadow:none">
    <svg viewBox="0 0 353 100" preserveAspectRatio="none"><path d="M0 0H353V60Q176 110 0 60Z" fill="var(--black)"/></svg>
    <div class="brand" style="color:#fff"><span class="brand-dot"></span>Deep Reef Co</div>
  </section>
  <section class="piece flap" style="top:118px;height:82px;box-shadow:none">
    <svg viewBox="0 0 353 82" preserveAspectRatio="none"><path d="M0 0H353V48Q176 90 0 48Z" fill="var(--grey)"/></svg>
  </section>
  <section class="piece flap" style="top:206px;height:76px;box-shadow:none">
    <svg viewBox="0 0 353 76" preserveAspectRatio="none"><defs><linearGradient id="flapBlue" x1="0" x2="1"><stop offset="0" stop-color="#1f5fae"/><stop offset=".5" stop-color="#5aa3e6"/><stop offset="1" stop-color="#1f5fae"/></linearGradient></defs><path d="M0 0H353V44Q176 84 0 44Z" fill="url(#flapBlue)"/></svg>
  </section>
  <section class="piece flap" style="top:286px;height:70px;box-shadow:none">
    <svg viewBox="0 0 353 70" preserveAspectRatio="none"><path d="M0 0H353V40Q176 78 0 40Z" fill="var(--pale)"/></svg>
  </section>

  <!-- envelope front -->
  <section class="piece envelope">
    <div class="brand"><span class="brand-dot"></span>Deep Reef Co</div>
    <div class="ret">4810 Harbor Ct, Dunedin FL 34512</div>
    <div class="mark mark-fill" role="img" aria-label="Faint hammerhead shark line illustration"></div>
  </section>

</main>
</body>
</html>
```